Corra-Linwick Custom Jewelry Homepage

High-end custom jewelry designer ($10,000-$1 mil.) website design. PSD only for WordPress framework.

Corra Linwick has a temporary site at http://corra-linwick.example/ and is looking for a permanent design.

We need an elegant WordPress homepage designed that highlights our client's products and presents them as high-end, exclusive pieces of jewelry that are custom designed for each client.

Please see that attached design brief for more information.
Updates

Project Deadline Extended
Reason: Hi Guys, We need a little more time to meet with our client and choose a final design. Thanks,

Project Deadline Extended

Target Market(s)

High end jewelry buyers

Industry/Entity Type

Jewelry

Number of Pages Required

1 page

Requirements
Must have
• Homepage design similar to attached mockups with elegant product banner at top featuring the Corra Linwick logo in the 4 corners

```html
<!DOCTYPE html>
<html lang="en">
<head>
<meta charset="utf-8">
<title>Corra-Linwick Custom Jewelry</title>
<link href="https://fonts.googleapis.com/css2?family=Jost:wght@400;500;600&family=Great+Vibes&display=swap" rel="stylesheet">
<style>
  :root {
    --bg: #0d0e12;
    --bg-soft: #15161b;
    --text: #ffffff;
    --muted: #8a8576;
    --frame: #a9a9a9;
    --stone-bright: rgba(225, 226, 230, 0.85);
    --stone-mid: rgba(150, 151, 158, 0.55);
    --stone-low: rgba(80, 81, 88, 0.35);
    --stone-none: rgba(13, 14, 18, 0);
  }
  * { margin: 0; padding: 0; box-sizing: border-box; }
  html, body { width: 1200px; height: 761px; overflow: hidden; background: var(--bg); }
  body { font-family: "Jost", sans-serif; color: var(--text); }
  .hero {
    position: relative; width: 1200px; height: 761px; overflow: hidden;
    background: radial-gradient(ellipse at 70% 60%, var(--bg-soft) 0%, var(--bg) 65%);
  }
  .menu-toggle { position: absolute; left: 46px; top: 28px; width: 32px; height: 16px; }
  .menu-toggle span { display: block; height: 2px; background: var(--text); margin-bottom: 4px; }
  .account-nav { position: absolute; top: 19px; right: 49px; display: flex; gap: 24px; font-size: 14px; }
  .account-nav a { color: var(--text); text-decoration: none; }
  .account-nav .currency { margin-left: 8px; }
  .social-nav { position: absolute; top: 70px; right: 48px; display: flex; gap: 12px; font-size: 12px; }
  .social-nav a { color: var(--text); text-decoration: none; }
  .brand {
    position: absolute; top: 78px; left: 0; width: 1200px;
    display: flex; justify-content: center; align-items: center; gap: 10px;
    font-size: 26px; font-weight: 500; letter-spacing: 1px; line-height: 36px;
  }
  .brand-dot { width: 14px; height: 14px; border: 2px solid var(--text); border-radius: 50%; }
  .ring-photo {
    position: absolute; left: 470px; top: 250px; width: 730px; height: 511px;
    background:
      radial-gradient(ellipse 22% 30% at 80% 42%, var(--stone-bright) 0%, var(--stone-mid) 55%, var(--stone-none) 100%),
      radial-gradient(ellipse 46% 30% at 58% 52%, var(--stone-mid) 0%, var(--stone-low) 55%, var(--stone-none) 100%),
      radial-gradient(ellipse 45% 12% at 60% 86%, var(--stone-low) 0%, var(--stone-none) 100%);
  }
  .hero-copy { position: absolute; left: 48px; top: 248px; width: 520px; }
  .hero-script { font-family: "Great Vibes", cursive; font-size: 40px; line-height: 52px; }
  .hero-price, .hero-title { font-size: 43px; font-weight: 600; line-height: 52px; letter-spacing: 1px; text-transform: uppercase; }
  .hero-price { color: var(--muted); margin-top: 2px; }
  .hero-text { font-size: 16px; line-height: 22px; width: 420px; margin: 6px 0 0 3px; }
  .shop-button {
    display: inline-block; margin: 24px 0 0 4px; width: 127px; height: 43px;
    border: 2px solid var(--frame); color: var(--text); text-decoration: none;
    font-size: 17px; font-weight: 600; line-height: 39px; text-align: center; letter-spacing: 0.5px;
  }
</style>
</head>
<body>
<main class="hero">
  <div class="menu-toggle" aria-label="Menu"><span></span><span></span><span></span></div>

  <nav class="account-nav">
    <a href="#">Login</a>
    <a href="#">Wish List</a>
    <a href="#">Cart(0)</a>
    <a href="#" class="currency">USD</a>
  </nav>

  <nav class="social-nav">
    <a href="#">Folio</a>
    <a href="#">Orbit</a>
    <a href="#">Relay</a>
    <a href="#">Tackle</a>
    <a href="#">Crest</a>
  </nav>

  <div class="brand"><span class="brand-dot"></span>Corra Linwick</div>

  <div class="ring-photo" role="img" aria-label="Diamond engagement ring with pavé band on a dark reflective surface"></div>

  <section class="hero-copy">
    <p class="hero-script">Corra Linwick</p>
    <h2 class="hero-price">From $10,000-$1 Mil</h2>
    <h1 class="hero-title">Jewelry Collection</h1>
    <p class="hero-text">Aenean sollicitudin, lorem quis bibendum auctor, nisi elit consequat ipsum, nec sagittis sem nibh id elit. Duis sed odio sit amet nibh</p>
    <a href="#" class="shop-button">SHOP NOW</a>
  </section>
</main>
</body>
</html>
```